Bref créative
business cards & stationary
Corvell Insulation
Modern
BO KERRIGAN
SALESMAN
14 PELLMORE CT.
MARLOWE, CA 94021
bo.kerrigan@corvellinsulation.com
www.corvellinsulation.com
I'd like the edges to be rounded instead of pointed. I would also like little symbols next to the phone, E-mail, website, and fax. For example, near the phone number, a small telephone. Also, if possible, I would like a QR Barcode that leads to my website on the back.

```html
<!DOCTYPE html>
<html lang="en">
<head>
<meta charset="utf-8">
<title>Corvell Insulation – Business Card</title>
<link href="https://fonts.googleapis.com/css2?family=Montserrat:wght@400;500;600;700;800&display=swap" rel="stylesheet">
<style>
  :root {
    --bg: #e9ebe7;
    --card: #ffffff;
    --ink: #3a3d3f;
    --ink-soft: #6b6f72;
    --rule: #d4d6d3;
    --green: #3aa335;
    --green-dark: #1f7a2a;
    --green-light: #8bd13f;
    --white: #ffffff;
    --shadow: rgba(0,0,0,0.18);
  }
  * { margin: 0; padding: 0; box-sizing: border-box; }
  html, body { width: 1200px; height: 629px; overflow: hidden; }
  body {
    background: var(--bg);
    font-family: "Montserrat", sans-serif;
    color: var(--ink);
    display: flex;
    align-items: center;
    justify-content: center;
    gap: 60px;
  }
  .card {
    position: relative;
    width: 520px;
    height: 297px;
    background: var(--card);
    border-radius: 16px;
    box-shadow: 0 10px 30px var(--shadow);
    overflow: hidden;
  }

  /* Back side */
  .back-mark {
    position: absolute;
    left: 40px;
    bottom: 40px;
    width: 150px;
    height: 150px;
    border-radius: 18px;
    background: linear-gradient(135deg, var(--green-light), var(--green-dark));
  }
  .back-name {
    position: absolute;
    right: 36px;
    top: 48px;
    text-align: right;
    font-weight: 700;
    color: var(--ink);
    line-height: 1.05;
  }
  .back-name .name-main { display: block; font-size: 40px; letter-spacing: 2px; }
  .back-name .name-sub { display: block; font-size: 17px; letter-spacing: 3px; }

  /* Front side */
  .brand {
    position: absolute;
    left: 150px;
    top: 36px;
    display: flex;
    align-items: center;
    gap: 12px;
  }
  .brand-square {
    width: 38px;
    height: 38px;
    border-radius: 6px;
    background: var(--green);
  }
  .brand-name {
    font-weight: 700;
    color: var(--ink);
    line-height: 1.05;
  }
  .brand-name .name-main { display: block; font-size: 30px; letter-spacing: 1.5px; }
  .brand-name .name-sub { display: block; font-size: 13px; letter-spacing: 2.5px; }

  .person {
    position: absolute;
    left: 150px;
    top: 140px;
    width: 140px;
    text-align: right;
  }
  .person-name { font-size: 11px; font-weight: 700; color: var(--green); letter-spacing: 1px; }
  .person-title { font-size: 8px; font-weight: 500; color: var(--ink-soft); letter-spacing: 1.5px; margin-top: 2px; }

  .address {
    position: absolute;
    left: 150px;
    top: 200px;
    width: 140px;
    text-align: right;
    font-size: 7.5px;
    line-height: 1.6;
    color: var(--ink-soft);
    letter-spacing: 0.8px;
    font-weight: 500;
  }

  .divider {
    position: absolute;
    left: 298px;
    top: 132px;
    width: 1px;
    height: 96px;
    background: var(--rule);
  }

  .contacts {
    position: absolute;
    left: 305px;
    top: 130px;
    list-style: none;
    font-size: 8px;
    color: var(--ink-soft);
    font-weight: 500;
    letter-spacing: 0.4px;
  }
  .contacts li { display: flex; align-items: center; gap: 6px; height: 15px; white-space: nowrap; }
  .contact-icon {
    width: 11px; height: 11px;
    border-radius: 50%;
    background: var(--green);
    display: flex; align-items: center; justify-content: center;
    flex-shrink: 0;
  }
  .contact-icon svg { width: 7px; height: 7px; }

  .web-band {
    position: absolute;
    left: 0; right: 0; bottom: 0;
    height: 40px;
    background: linear-gradient(90deg, var(--white) 0%, var(--green-light) 35%, var(--green) 70%, var(--green-dark) 100%);
    display: flex;
    align-items: center;
    justify-content: center;
  }
  .web-band-line {
    position: absolute;
    left: 0; right: 0; top: 0;
    height: 3px;
    background: var(--green-dark);
  }
  .web-band-text {
    font-size: 8px;
    letter-spacing: 3px;
    color: var(--white);
    font-weight: 600;
    text-transform: uppercase;
  }
</style>
</head>
<body>

  <section class="card card-back" aria-label="Card back">
    <div class="back-mark"></div>
    <div class="back-name">
      <span class="name-main">CORVELL</span>
      <span class="name-sub">INSULATION</span>
    </div>
  </section>

  <section class="card card-front" aria-label="Card front">
    <div class="brand">
      <div class="brand-square"></div>
      <div class="brand-name">
        <span class="name-main">CORVELL</span>
        <span class="name-sub">INSULATION</span>
      </div>
    </div>

    <div class="person">
      <p class="person-name">BO KERRIGAN</p>
      <p class="person-title">SALESMAN</p>
    </div>

    <p class="address">14 PELLMORE CT.<br>MARLOWE, CA 94021</p>

    <div class="divider"></div>

    <ul class="contacts">
      <li>
        <span class="contact-icon"><svg viewBox="0 0 10 10"><path d="M2 1 L4 1 L4.6 3 L3.4 3.8 Q4.2 5.8 6.2 6.6 L7 5.4 L9 6 L9 8 Q5 9 1 5 Q1 3 2 1Z" fill="#fff"/></svg></span>
        (555) 201-0142
      </li>
      <li>
        <span class="contact-icon"><svg viewBox="0 0 10 10"><rect x="2" y="1" width="6" height="3" fill="#fff"/><rect x="1" y="4" width="8" height="4" rx="1" fill="#fff"/></svg></span>
        (555) 201-0187
      </li>
      <li>
        <span class="contact-icon"><svg viewBox="0 0 10 10"><rect x="3" y="1" width="4" height="8" rx="1" fill="#fff"/></svg></span>
        (555) 201-0163
      </li>
      <li>
        <span class="contact-icon"><svg viewBox="0 0 10 10"><rect x="1" y="2.5" width="8" height="5" fill="#fff"/><path d="M1 2.5 L5 6 L9 2.5" stroke="#3aa335" stroke-width="0.8" fill="none"/></svg></span>
        bo.kerrigan@corvellinsulation.com
      </li>
      <li>
        <span class="contact-icon"><svg viewBox="0 0 10 10"><circle cx="5" cy="5" r="3.6" fill="none" stroke="#fff" stroke-width="1"/><path d="M1.4 5 H8.6 M5 1.4 Q3 5 5 8.6 Q7 5 5 1.4" stroke="#fff" stroke-width="0.8" fill="none"/></svg></span>
        www.corvellinsulation.com
      </li>
    </ul>

    <div class="web-band">
      <div class="web-band-line"></div>
      <span class="web-band-text">www.corvellinsulation.com</span>
    </div>
  </section>

</body>
</html>
```